Real Estate Biz Card

-Card Size: Standard
-Background: Dark grey or black. I am open to gradient or a textured background.
-Other Colors: I dont mind pops of color. Contrasty blue, lime green, red Etc. Feel free to get creative.
-Text color: be creative
-Font: I like modern styles. Something that works well with my KV718 logo. See attached
-I would like my logo (KV718) watermarked on the card. Either on one side or both.
-Front of Card: keep it simple. Head shot, name, Logo, Phone #
-Back: add the rest of the details. See list below.
-brokerages logo as well as the Dwellon and Equal Housing Opportunity logos on the card
-Name: Milo Dravek
-Residential Real Estate
-Cell:
-Email:
-Site:
-Office Address:
-very small/fine print "Each office independently owned & operated

```html
<!DOCTYPE html>
<html lang="en">
<head>
<meta charset="utf-8">
<title>KV718 Business Card</title>
<link rel="stylesheet" href="https://fonts.googleapis.com/css2?family=Roboto:wght@300;400;500;700;900&display=swap">
<style>
  :root {
    --page: #2b2b2d;
    --card-top: #3a3b3e;
    --card-bottom: #232427;
    --ink: #ffffff;
    --ink-soft: #d9dbe0;
    --accent: #7a87a8;
    --accent-text: #8a97b8;
    --badge: #6d6f75;
    --photo-a: #3f4a66;
    --photo-b: #5a6d9c;
  }
  * { box-sizing: border-box; margin: 0; padding: 0; }
  html, body { width: 799px; height: 1200px; overflow: hidden; }
  body {
    background: var(--page);
    font-family: "Roboto", sans-serif;
    color: var(--ink);
    position: relative;
  }
  .card {
    position: absolute;
    left: 60px;
    width: 679px;
    height: 388px;
    background: linear-gradient(160deg, var(--card-top), var(--card-bottom));
    overflow: hidden;
    box-shadow: 0 14px 30px rgba(0,0,0,.45);
  }
  .card--back { top: 110px; }
  .card--front { top: 700px; }

  .brand {
    display: flex;
    align-items: center;
    gap: 14px;
    font-weight: 900;
    letter-spacing: 2px;
    color: var(--ink);
    line-height: 1;
  }
  .brand__mark {
    background: var(--ink);
    display: block;
  }

  /* back side */
  .card--back .brand {
    position: absolute;
    left: 150px;
    top: 70px;
    font-size: 110px;
  }
  .card--back .brand__mark { width: 26px; height: 26px; }
  .contact {
    position: absolute;
    left: 150px;
    top: 215px;
    font-size: 19px;
    color: var(--ink-soft);
    line-height: 1.55;
  }
  .contact .sep { margin: 0 10px; }
  .band {
    position: absolute;
    left: 0; right: 0; bottom: 0;
    height: 60px;
    background: var(--accent);
    display: flex;
    align-items: center;
    padding-left: 150px;
    font-size: 18px;
    color: var(--ink);
  }

  /* front side */
  .card--front .brand {
    position: absolute;
    left: 40px;
    top: 40px;
    font-size: 82px;
  }
  .card--front .brand__mark { width: 20px; height: 20px; }
  .agent {
    position: absolute;
    left: 40px;
    top: 150px;
  }
  .agent__name {
    font-size: 28px;
    font-weight: 500;
    letter-spacing: 2px;
    text-transform: uppercase;
    color: var(--accent-text);
  }
  .agent__title { font-size: 17px; color: var(--ink-soft); margin-top: 4px; }
  .agent__phone {
    display: flex; align-items: center; gap: 10px;
    font-size: 24px; margin-top: 8px;
  }
  .badges {
    position: absolute;
    left: 40px;
    top: 272px;
    display: flex;
    align-items: center;
    gap: 22px;
  }
  .badge { background: var(--badge); border-radius: 3px; }
  .badge--broker { width: 80px; height: 26px; }
  .badge--housing { width: 30px; height: 26px; }
  .badge-label {
    display: flex; align-items: center; gap: 6px;
    font-size: 13px; font-weight: 500; color: var(--badge);
    text-transform: uppercase; letter-spacing: 1px;
  }
  .badge-label::before {
    content: ""; width: 20px; height: 20px; background: var(--badge);
  }
  .card--front .band {
    padding-left: 40px;
    text-transform: uppercase;
    letter-spacing: 1px;
    font-size: 17px;
    right: 260px;
    height: 54px;
  }
  .headshot {
    position: absolute;
    right: 0;
    bottom: 0;
    width: 280px;
    height: 270px;
    background: radial-gradient(ellipse at 50% 30%, var(--photo-b), var(--photo-a) 70%, transparent 100%);
  }
</style>
</head>
<body>

<section class="card card--back" aria-label="Card back">
  <div class="brand"><span class="brand__mark"></span>KV718</div>
  <div class="contact">
    <p>info@kv718homes.com<span class="sep">|</span>www.kv718homes.com</p>
    <p>48 Alder Row North Ridge City 84190</p>
  </div>
  <div class="band">Each office independently owned &amp; operated</div>
</section>

<section class="card card--front" aria-label="Card front">
  <div class="brand"><span class="brand__mark"></span>KV718</div>
  <div class="agent">
    <p class="agent__name">Milo Dravek</p>
    <p class="agent__title">Real Estate Broker</p>
    <p class="agent__phone">
      <svg width="18" height="18" viewBox="0 0 24 24" aria-hidden="true">
        <path fill="#9aa0aa" d="M6.6 10.8a15.1 15.1 0 0 0 6.6 6.6l2.2-2.2a1 1 0 0 1 1-.25 11.4 11.4 0 0 0 3.6.57 1 1 0 0 1 1 1V20a1 1 0 0 1-1 1A17 17 0 0 1 3 4a1 1 0 0 1 1-1h3.5a1 1 0 0 1 1 1c0 1.25.2 2.45.57 3.57a1 1 0 0 1-.25 1z"/>
      </svg>
      555.302.4186
    </p>
  </div>
  <div class="badges">
    <span class="badge badge--broker"></span>
    <span class="badge badge--housing"></span>
    <span class="badge-label">Dwellon</span>
  </div>
  <div class="band">Residential Real Estate</div>
  <div class="headshot" role="img" aria-label="Headshot of the agent in a blue shirt"></div>
</section>

</body>
</html>
```